FR / EN Beekeeper research design packaging / label; Beekeeper looking for a design package

I need as a beekeeper to create a design to better showcase my honey. Indeed I work in a natural environment of high quality on a hill called "Veldmoor" (many flowers different fields, few pesticides, ...). I practice a beekeeping respectful of the bee and in a traditional way. I produce a high quality honey (luxury product) for a wealthy clientele looking for good health products, ... The main label should contain only the following text (accompanied by an image): The Veldmoor Honey A variant would also be useful for my production of mead (alcohol from the fermentation of honey): The Veldmoor mead In terms of form, given the target audience, I thought I was moving towards a modern label against a background black and with golden patterns. An example is the honey of the wonders attached, we find a honey assimilated as a real luxury product. Same in the Cuvée Lando Perrusi attachment. I would like to move towards these tones of colors by adding a touch more "champêtre" as on the label of the bottle of wine below where one sees golden flowers drawn, of light and subtle way. Another example that I like is that of the bee of ree joined. Another modern idea identified on this site is this design: https://www.artpitchhub.com/design/30418822 https: //www.artpitchhub. com / design / 30418957 I would also need a round label to place on the lid of the pot with indications of signs (my address) as well as additional information about my product: - BALDUCCI Armand - Veldmoor, 14 - 6812 Hautvelin - 500 g - Spring harvest - Honey all flowers - Flora: rapeseed, fruit trees, clovers - Flavors: sweet honey with vegetal notes Remarks: this is my first artpitchhub project, if you are surprised by some points of the brief or it is missing important information do not hesitate to let me know! ************************************************** ******************************* ENGLISH ****************** ************** I need to beekeeper a new design Indeed, I work in a very natural environment, a high quality eco-system which is the south of Belgium (many different flowers in the fields, few pesticides, ...). I practice a natural beekeeping, in an artisanal way I produce a high quality honey (luxuous product) for wealthy people who are looking for good and healthy products. The following description: The Veldmoor Honey A slight variation could be useful for my production (alcohol from honey fermentation): The Veldmoor Meads Concerning the form, a modern design with golden patterns on a black background could be appropriate. An example is the honey of the wonders in attachment, we could see that honey in this case is a branded like a very luxuous product. I wish to go for these last colors with a more "rural touch" as attachment. We can see golden flowers in a light and elegant manner. Another interesting example is the honey bee in attachment. Some example found on this site: https://www.artpitchhub.com/design/30418822 https: //www.artpitchhub. com / design / 30418957 Balducci Armand - Veldmoor, 14 - 6812 Hautvelin - 500 g - Spring Harvest - Honey all flowers - Flora: rapeseed, fruit, clovers - Flavors: sweet honey with vegetal notes

Target Market(s)

affluent clientele looking for natural products, good for health, ...

Industry/Entity Type

Agriculture

Font styles to use
Decorative
Script
Other font styles liked:
• à la libre appréciation du designer, tant que c'est moderne et élégant

Requirements
Must have
• All text must be in French / A main label and a round label on the lid of the jar. Gilding (preferably on a black background). An image accompanying the text. Gold on a black background
Nice to have
• Elegant and modern design Elegant and modern design
Should not have
• Do not load too much the main label, it must remain uncluttered

```html
<!DOCTYPE html>
<html lang="fr">
<head>
<meta charset="utf-8">
<title>Le Miel du Veldmoor – étiquette de couvercle</title>
<link rel="stylesheet" href="https://fonts.googleapis.com/css2?family=Almendra:wght@400;700&family=Roboto:wght@400&family=Libre+Baskerville:wght@700&display=swap">
<style>
  :root {
    --paper: #f2e6d3;
    --gold: #c9973a;
    --gold-muted: #8a6a2c;
    --black: #000000;
    --brown: #1e0f08;
  }
  html, body {
    margin: 0;
    width: 1200px;
    height: 603px;
    overflow: hidden;
    background: var(--paper);
  }
  .board {
    position: relative;
    width: 1200px;
    height: 603px;
  }
  .lid-label {
    position: absolute;
    top: 56px;
    width: 490px;
    height: 490px;
  }
  .lid-label--black { left: 56px; --ground: var(--black); }
  .lid-label--brown { left: 653px; --ground: var(--brown); }
  .lid-label svg { width: 490px; height: 490px; display: block; }
  .rim { fill: var(--gold); }
  .ground { fill: var(--ground); }
  .inner-line { fill: none; stroke: var(--gold); stroke-width: 1; }
  .title { font-family: "Almendra", serif; fill: var(--gold); }
  .title-small { font-size: 40px; }
  .title-big { font-size: 72px; }
  .emblem { fill: var(--gold-muted); }
  .info { font-family: "Roboto", Arial, sans-serif; fill: var(--gold); }
  .harvest { font-size: 15.5px; }
  .flavours { font-size: 13.5px; }
  .details { font-size: 12.5px; }
  .address { font-size: 12.5px; }
  .weight { font-family: "Libre Baskerville", Georgia, serif; font-weight: 700; font-size: 19px; fill: var(--gold); }
  .swatch {
    position: absolute;
    top: 556px;
    width: 31px;
    height: 31px;
  }
  .swatch--gold { background: var(--gold); }
  .swatch--black { background: var(--black); }
  .swatch--brown { background: var(--brown); }
</style>
</head>
<body>
<main class="board">

  <section class="lid-label lid-label--black">
    <svg viewBox="0 0 490 490" aria-label="Étiquette de couvercle, fond noir">
      <defs>
        <path id="address-arc-a" d="M 40,245 A 205 205 0 0 0 450,245"/>
      </defs>
      <circle class="rim" cx="245" cy="245" r="244"/>
      <circle class="ground" cx="245" cy="245" r="235"/>
      <circle class="inner-line" cx="245" cy="245" r="229"/>
      <text class="title" x="113" y="108"><tspan class="title-small">Le </tspan><tspan class="title-big">Miel</tspan></text>
      <text class="title" x="50" y="198"><tspan class="title-small">du </tspan><tspan class="title-big">Veldmoor</tspan></text>
      <rect class="emblem" x="174" y="215" width="146" height="71" rx="6" role="img" aria-label="Illustration dorée : alvéoles de ruche et abeille"/>
      <text class="info harvest" x="245" y="319" text-anchor="middle">Récolte de printemps</text>
      <text class="info flavours" x="245" y="343" text-anchor="middle">Saveurs : miel doux aux notes végétales</text>
      <text class="info details" x="163" y="385">Miel toutes fleurs</text>
      <text class="info details" x="163" y="405">Flore : colza, fruitiers, trèfles</text>
      <text class="weight" transform="translate(446 245) rotate(90)" text-anchor="middle">500 g</text>
      <text class="info address"><textPath href="#address-arc-a" startOffset="50%" text-anchor="middle">BALDUCCI Armand Veldmoor, 14 - 6812 Hautvelin</textPath></text>
    </svg>
  </section>

  <section class="lid-label lid-label--brown">
    <svg viewBox="0 0 490 490" aria-label="Étiquette de couvercle, fond brun foncé">
      <defs>
        <path id="address-arc-b" d="M 40,245 A 205 205 0 0 0 450,245"/>
      </defs>
      <circle class="rim" cx="245" cy="245" r="244"/>
      <circle class="ground" cx="245" cy="245" r="235"/>
      <circle class="inner-line" cx="245" cy="245" r="229"/>
      <text class="title" x="113" y="108"><tspan class="title-small">Le </tspan><tspan class="title-big">Miel</tspan></text>
      <text class="title" x="50" y="198"><tspan class="title-small">du </tspan><tspan class="title-big">Veldmoor</tspan></text>
      <rect class="emblem" x="174" y="215" width="146" height="71" rx="6" role="img" aria-label="Illustration dorée : alvéoles de ruche et abeille"/>
      <text class="info harvest" x="245" y="319" text-anchor="middle">Récolte de printemps</text>
      <text class="info flavours" x="245" y="343" text-anchor="middle">Saveurs : miel doux aux notes végétales</text>
      <text class="info details" x="163" y="385">Miel toutes fleurs</text>
      <text class="info details" x="163" y="405">Flore : colza, fruitiers, trèfles</text>
      <text class="weight" transform="translate(446 245) rotate(90)" text-anchor="middle">500 g</text>
      <text class="info address"><textPath href="#address-arc-b" startOffset="50%" text-anchor="middle">BALDUCCI Armand Veldmoor, 14 - 6812 Hautvelin</textPath></text>
    </svg>
  </section>

  <div class="swatch swatch--gold" style="left:24px"></div>
  <div class="swatch swatch--black" style="left:60px"></div>
  <div class="swatch swatch--gold" style="left:620px"></div>
  <div class="swatch swatch--brown" style="left:656px"></div>

</main>
</body>
</html>
```